Brook & Thistle Labels*

Hello :) I am needing labels for my herbal tea/petal product. I am a small producer for the local restaurants (edible flowers/micro herbs & dried product). I am hoping to sell the dried product online. It will be sold in batches as it is ready so quite small/boutique and the label needs to be somewhat generic for the range of produce I make.
Feels: no/minimal plastic, product is in a reusable mason jar, we use organic/regenerative principles from soil health to end product. Treading gently on the land. High quality i.e only fresh hand picked leaf tips for the tea.

```html
<!DOCTYPE html>
<html lang="en">
<head>
<meta charset="utf-8">
<title>Brook &amp; Thistle — Label Range</title>
<link href="https://fonts.googleapis.com/css2?family=Josefin+Sans:wght@300;400;600&family=Courier+Prime&family=Allura&display=swap" rel="stylesheet">
<style>
  :root {
    --paper: #ffffff;
    --ink: #1d1d1d;
    --line: #3a3a3a;
    --brand-green: #4fe010;
    --calendula: #e8b59a;
    --calendula-badge: #e2a184;
    --calendula-photo-a: #e86a1c;
    --calendula-photo-b: #c8470c;
    --cornflower: #c0dfe9;
    --cornflower-badge: #aed2e3;
    --cornflower-photo-a: #3f5ae6;
    --cornflower-photo-b: #2a3cc4;
    --thistle: #ebcde6;
    --thistle-badge: #e6c1e2;
    --thistle-photo-a: #e4e2ea;
    --thistle-photo-b: #b9a3cc;
    --annotation: #e0281e;
  }
  * { box-sizing: border-box; margin: 0; padding: 0; }
  html, body { width: 1200px; height: 1054px; overflow: hidden; background: var(--paper); }
  body { position: relative; font-family: "Josefin Sans", sans-serif; color: var(--ink); }

  .label {
    position: absolute; top: 55px; width: 195px; height: 350px;
    border: 1px solid var(--line); border-radius: 8px; background: var(--paper); overflow: hidden;
  }
  .label--calendula { left: 270px; top: 56px; --tone: var(--calendula); --badge: var(--calendula-badge); --photo-a: var(--calendula-photo-a); --photo-b: var(--calendula-photo-b); }
  .label--cornflower { left: 544px; --tone: var(--cornflower); --badge: var(--cornflower-badge); --photo-a: var(--cornflower-photo-a); --photo-b: var(--cornflower-photo-b); }
  .label--thistle { left: 780px; --tone: var(--thistle); --badge: var(--thistle-badge); --photo-a: var(--thistle-photo-a); --photo-b: var(--thistle-photo-b); }

  .brand { position: absolute; left: 11px; top: 30px; display: flex; align-items: center; gap: 4px; }
  .brand__dot { width: 16px; height: 16px; border-radius: 50%; background: var(--brand-green); }
  .brand__name { font-weight: 600; font-size: 13px; line-height: 1; color: var(--brand-green); padding-top: 2px; }

  .claim { position: absolute; left: 134px; top: 13px; width: 56px; text-align: center; }
  .claim__badge { width: 32px; height: 32px; border-radius: 50%; background: var(--badge); margin: 0 auto; }
  .claim__text { font-family: "Allura", cursive; font-size: 12px; line-height: 1; margin-top: 4px; white-space: nowrap; }

  .photo {
    position: absolute; left: 40px; top: 68px; width: 112px; height: 104px; border-radius: 6px;
    background: linear-gradient(160deg, var(--photo-a), var(--photo-b));
  }

  .panel {
    position: absolute; left: 0; top: 182px; width: 100%; height: 137px;
    background: var(--tone); text-align: center;
  }
  .panel__kicker { position: absolute; left: 0; right: 0; top: 16px; font-family: "Allura", cursive; font-size: 19px; line-height: 1; }
  .panel__name { position: absolute; left: 0; right: 0; top: 45px; font-weight: 400; font-size: 15px; line-height: 1; letter-spacing: 0.14em; padding-left: 0.14em; white-space: nowrap; }
  .panel__rule { position: absolute; left: 87px; top: 70px; width: 21px; height: 2px; background: var(--ink); }
  .panel__story { position: absolute; left: 0; right: 0; top: 83px; font-family: "Courier Prime", monospace; font-size: 8px; line-height: 11px; letter-spacing: 0.02em; word-spacing: 0.2em; text-transform: uppercase; }

  .spec { position: absolute; left: 0; top: 319px; width: 100%; height: 31px; font-size: 10px; letter-spacing: 0.2em; }
  .spec__brew { position: absolute; left: 17px; top: 11px; line-height: 1; white-space: nowrap; }
  .spec__divider { position: absolute; left: 110px; top: 7px; height: 17px; border-left: 1px dotted var(--line); }
  .spec__weight { position: absolute; left: 121px; top: 11px; line-height: 1; white-space: nowrap; }

  .note { position: absolute; left: 115px; top: 384px; font-size: 13px; line-height: 1; letter-spacing: 0.22em; white-space: nowrap; }
  .note__arrow { position: absolute; left: 227px; top: 386px; }
  .note__frame { position: absolute; left: 283px; top: 382px; width: 167px; height: 18px; border: 1px solid var(--annotation); }
</style>
</head>
<body>

  <article class="label label--calendula">
    <div class="brand"><span class="brand__dot"></span><span class="brand__name">fernwold</span></div>
    <div class="claim"><div class="claim__badge"></div><div class="claim__text">chemical-free</div></div>
    <div class="photo" role="img" aria-label="Photograph of an orange calendula flower head"></div>
    <div class="panel">
      <p class="panel__kicker">Fresh Hand-Picked</p>
      <h2 class="panel__name">BROOK &amp; THISTLE</h2>
      <div class="panel__rule"></div>
      <p class="panel__story">Grown, harvested and dried<br>chemical free on our farm in<br>East Gippsland</p>
    </div>
    <div class="spec"><span class="spec__brew">212 F / 3MIN</span><span class="spec__divider"></span><span class="spec__weight">00 GRAM</span></div>
  </article>

  <article class="label label--cornflower">
    <div class="brand"><span class="brand__dot"></span><span class="brand__name">fernwold</span></div>
    <div class="claim"><div class="claim__badge"></div><div class="claim__text">chemical-free</div></div>
    <div class="photo" role="img" aria-label="Photograph of blue cornflowers arranged in a heart shape"></div>
    <div class="panel">
      <p class="panel__kicker">Fresh Hand-Picked</p>
      <h2 class="panel__name">BROOK &amp; THISTLE</h2>
      <div class="panel__rule"></div>
      <p class="panel__story">Grown, harvested and dried<br>chemical free on our farm in<br>East Gippsland</p>
    </div>
    <div class="spec"><span class="spec__brew">212 F / 3MIN</span><span class="spec__divider"></span><span class="spec__weight">00 GRAM</span></div>
  </article>

  <article class="label label--thistle">
    <div class="brand"><span class="brand__dot"></span><span class="brand__name">fernwold</span></div>
    <div class="claim"><div class="claim__badge"></div><div class="claim__text">chemical-free</div></div>
    <div class="photo" role="img" aria-label="Photograph of a white and purple cornflower head"></div>
    <div class="panel">
      <p class="panel__kicker">Fresh Hand-Picked</p>
      <h2 class="panel__name">BROOK &amp; THISTLE</h2>
      <div class="panel__rule"></div>
      <p class="panel__story">Grown, harvested and dried<br>chemical free on our farm in<br>East Gippsland</p>
    </div>
    <div class="spec"><span class="spec__brew">212 F / 3MIN</span><span class="spec__divider"></span><span class="spec__weight">00 GRAM</span></div>
  </article>

  <span class="note">DUMMY TEXT</span>
  <svg class="note__arrow" width="55" height="10" viewBox="0 0 55 10" aria-hidden="true">
    <line x1="0" y1="5" x2="49" y2="5" stroke="#e0281e" stroke-width="1"/>
    <polygon points="49,2 54,5 49,8" fill="#e0281e"/>
  </svg>
  <div class="note__frame"></div>

</body>
</html>
```